I need a graphic for the promotion email for our "8th Annual Brightwater Field Drills Academy" that incorporates our current logo and brand theme. I would like this graphic to funnel potentional attendees to register for a course. My perference would include a cool fire photo from our facility for the background. More information can be found on Kestrelvale.com and also our Facebook.

```html
<!DOCTYPE html>
<html lang="en">
<head>
<meta charset="utf-8">
<title>Brightwater Field Drills Academy – Register</title>
<link href="https://fonts.googleapis.com/css2?family=Bebas+Neue&family=Roboto+Condensed:wght@400;500&family=Montserrat:wght@500;600&display=swap" rel="stylesheet">
<style>
  :root{
    --slate-dark:#27313b;
    --slate:#3e4a55;
    --mist:#e9ebec;
    --ink:#1d1f22;
    --brand-red:#e8401c;
    --cta-orange:#f04a0c;
    --signal-yellow:#ffee00;
    --white:#ffffff;
    --footer:#22252a;
  }
  *{margin:0;padding:0;box-sizing:border-box}
  html,body{width:1200px;height:1200px;overflow:hidden;background:var(--white)}
  .poster{
    position:relative;width:1200px;height:1200px;overflow:hidden;
    background:
      radial-gradient(ellipse 520px 380px at 50% 0%, var(--mist) 0%, #b7bcc1 35%, var(--slate) 75%, var(--slate-dark) 100%);
    font-family:"Roboto Condensed", sans-serif;color:var(--white);
  }
  .scene-photo{
    position:absolute;left:0;top:600px;width:1200px;height:510px;
    background:
      radial-gradient(ellipse 180px 240px at 48% 30%, rgba(246,140,40,.85), rgba(200,80,20,.35) 55%, transparent 75%),
      radial-gradient(ellipse 200px 120px at 76% 58%, rgba(240,120,30,.7), transparent 70%),
      radial-gradient(ellipse 260px 160px at 62% 62%, rgba(215,222,228,.55), transparent 70%),
      linear-gradient(180deg, rgba(39,49,59,0) 0%, #4a5660 30%, #3a434b 70%, #2a2f35 100%);
  }
  .brand{position:absolute;left:0;top:42px;width:1200px;text-align:center}
  .brand-mark{display:block;margin:0 auto 22px;width:140px;height:140px;border-radius:50%;background:var(--brand-red)}
  .brand-name{font-family:"Montserrat", sans-serif;font-weight:600;font-size:34px;letter-spacing:6px;color:var(--ink);white-space:nowrap}
  .headline{
    position:absolute;left:0;top:306px;width:1200px;text-align:center;
    font-family:"Bebas Neue", sans-serif;font-size:124px;line-height:106px;font-weight:400;
    white-space:nowrap;text-shadow:0 4px 14px rgba(0,0,0,.45);
  }
  .tagline{
    position:absolute;left:0;top:556px;width:1200px;text-align:center;
    font-family:"Bebas Neue", sans-serif;font-size:58px;color:var(--signal-yellow);
    white-space:nowrap;text-shadow:0 2px 8px rgba(0,0,0,.4);
  }
  .courses{position:absolute;left:58px;top:666px;list-style:none}
  .course{display:flex;align-items:flex-start;height:78px}
  .course-icon{width:62px;height:62px;flex:none;margin-right:22px}
  .course-text{font-size:25px;line-height:26px;white-space:nowrap;text-shadow:0 1px 4px rgba(0,0,0,.6)}
  .course-hours{color:var(--signal-yellow)}
  .course.tall{height:91px}
  .date-badge{position:absolute;left:544px;top:678px;width:180px;height:202px}
  .date-badge text{font-family:"Roboto Condensed", sans-serif;text-anchor:middle}
  .cta{position:absolute;left:779px;top:729px;width:361px;text-align:center}
  .cta-button{
    display:block;background:var(--cta-orange);border-radius:6px;height:73px;
    font-family:"Bebas Neue", sans-serif;font-size:76px;line-height:80px;color:var(--white);
    white-space:nowrap;letter-spacing:-1px;overflow:hidden;
  }
  .cta-link{display:block;margin-top:10px;font-size:25px;color:var(--white);text-decoration:underline;white-space:nowrap}
  .footer{
    position:absolute;left:0;top:1108px;width:1200px;height:92px;background:var(--footer);
    font-family:"Montserrat", sans-serif;
  }
  .footer-label{position:absolute;left:54px;top:30px;font-size:24px;font-weight:600;color:var(--signal-yellow);white-space:nowrap}
  .footer-item{position:absolute;display:flex;align-items:center;color:var(--white);white-space:nowrap}
  .footer-item svg{margin-right:10px;flex:none}
  .footer-email{left:482px;top:28px;font-size:22px;font-weight:500}
  .footer-web{left:862px;top:28px;font-size:17px;font-weight:500}
</style>
</head>
<body>
<main class="poster">
  <div class="scene-photo" role="img" aria-label="Photograph of firefighters in turnout gear spraying water on a burning industrial training structure at the facility"></div>

  <header class="brand">
    <span class="brand-mark"></span>
    <div class="brand-name">KESTRELVALE RESCUE</div>
  </header>

  <h1 class="headline">8TH ANNUAL BRIGHTWATER<br>FIELD DRILLS ACADEMY</h1>
  <p class="tagline">ADVANCE YOUR SKILLS. LEAD YOUR TEAM.</p>

  <ul class="courses">
    <li class="course">
      <svg class="course-icon" viewBox="0 0 62 62"><circle cx="31" cy="31" r="26" fill="none" stroke="var(--signal-yellow)" stroke-width="6"/><path d="M31 16c3 7 10 10 10 18a10 10 0 0 1-20 0c0-5 3-7 5-10 1 4 3 5 4 5-1-5 0-9 1-13z" fill="var(--signal-yellow)"/></svg>
      <div class="course-text">Exterior Fire Brigade<br><span class="course-hours">(32 Hours)</span></div>
    </li>
    <li class="course tall">
      <svg class="course-icon" viewBox="0 0 62 62"><circle cx="31" cy="31" r="26" fill="none" stroke="var(--signal-yellow)" stroke-width="6"/><ellipse cx="31" cy="22" rx="9" ry="4" fill="none" stroke="var(--signal-yellow)" stroke-width="2.5"/><path d="M31 26v18M24 34l7-4 7 4M26 46l5-4 5 4" fill="none" stroke="var(--signal-yellow)" stroke-width="2.5"/></svg>
      <div class="course-text">Rope &amp; Confined Space<br>Rescue Technician<br><span class="course-hours">(40 Hours)</span></div>
    </li>
    <li class="course tall">
      <svg class="course-icon" viewBox="0 0 62 62"><circle cx="31" cy="31" r="26" fill="none" stroke="var(--signal-yellow)" stroke-width="6"/><circle cx="32" cy="19" r="3.5" fill="var(--signal-yellow)"/><path d="M31 24l-2 10 4 5-2 8M29 30l-5 4M31 28l6 3" fill="none" stroke="var(--signal-yellow)" stroke-width="3" stroke-linecap="round"/></svg>
      <div class="course-text">Advanced Rope &amp; Confined<br>Space Rescue Technician<br><span class="course-hours">(40 Hours)</span></div>
    </li>
    <li class="course">
      <svg class="course-icon" viewBox="0 0 62 62"><circle cx="31" cy="31" r="26" fill="none" stroke="var(--signal-yellow)" stroke-width="6"/><circle cx="31" cy="24" r="7" fill="none" stroke="var(--signal-yellow)" stroke-width="2.5"/><circle cx="24" cy="36" r="7" fill="none" stroke="var(--signal-yellow)" stroke-width="2.5"/><circle cx="38" cy="36" r="7" fill="none" stroke="var(--signal-yellow)" stroke-width="2.5"/><circle cx="31" cy="32" r="2.5" fill="var(--signal-yellow)"/></svg>
      <div class="course-text">Hazardous Materials Technician<br><span class="course-hours">(40 Hours)</span></div>
    </li>
    <li class="course">
      <svg class="course-icon" viewBox="0 0 62 62"><circle cx="31" cy="31" r="26" fill="none" stroke="var(--signal-yellow)" stroke-width="6"/><path d="M31 19v24M19 31h24" stroke="var(--signal-yellow)" stroke-width="5"/></svg>
      <div class="course-text">Emergency Medical Response<br><span class="course-hours">(40 Hours)</span></div>
    </li>
  </ul>

  <svg class="date-badge" viewBox="0 0 180 202">
    <polygon points="90,4 174,52 174,150 90,198 6,150 6,52" fill="var(--signal-yellow)" stroke="#ffd400" stroke-width="4"/>
    <text x="90" y="70" font-size="25" font-weight="500" fill="var(--ink)">CLASS</text>
    <text x="90" y="92" font-size="25" font-weight="500" fill="var(--ink)">RUNS</text>
    <text x="90" y="128" font-size="38" font-weight="500" fill="var(--brand-red)">May 4-7</text>
    <text x="90" y="164" font-size="38" font-weight="500" fill="var(--brand-red)">2026</text>
  </svg>

  <div class="cta">
    <span class="cta-button">REGISTER NOW</span>
    <span class="cta-link">Kestrelvale.com/register</span>
  </div>

  <footer class="footer">
    <span class="footer-label">Contact for More Information</span>
    <span class="footer-item footer-email">
      <svg width="30" height="30" viewBox="0 0 30 30"><circle cx="15" cy="15" r="13" fill="none" stroke="var(--white)" stroke-width="2"/><rect x="8" y="10" width="14" height="10" rx="1" fill="var(--white)"/><path d="M8 11l7 5 7-5" fill="none" stroke="var(--footer)" stroke-width="1.5"/></svg>
      Morgan@kestrelvale.com
    </span>
    <span class="footer-item footer-web">
      <svg width="34" height="34" viewBox="0 0 34 34"><circle cx="17" cy="17" r="15" fill="none" stroke="var(--white)" stroke-width="2"/><circle cx="17" cy="17" r="9" fill="none" stroke="var(--white)" stroke-width="1.5"/><ellipse cx="17" cy="17" rx="4" ry="9" fill="none" stroke="var(--white)" stroke-width="1.5"/><path d="M8 17h18M10 12h14M10 22h14" stroke="var(--white)" stroke-width="1.2"/></svg>
      www.kestrelvale.com
    </span>
  </footer>
</main>
</body>
</html>
```